Business card website / business card for website

We are a French website selling products Made in USA of quality, we need a business card to give from hand to hand and for deposit in the cartons of Each order. We-have the logo That I send in the attachments The theme is: US Vintage and find the compromised entre les national park ambience us and the atmosphere Brooklyn If you can make the feeling it's great The site www.lecomptoirdubisonroux.com (opening April) You can change the logo a little gold in color it could ... we are a French website selling products Made in USA quality, we need a business card to give from hand to hand and deposit in cartons each order. we have the logo that I convey in the attached parts is the theme: Vintage embiance US and find a compromise between the atmosphere us national park and the atmosphere Brooklyn at: www.lecomptoirdubisonroux.com (opening April) if you can the impression is great

Target Market(s)

25-50 YEARS man, woman.

Industry/Entity Type

Business

Contact Information for Business Card

www.lecomptoirdubisonroux.com
N'oubliez pas que nous sommes là si vous avez besoin de nouscontact@lecomptoirdubisonroux.com

Font styles to use
Serif

Requirements
Must have
• my logo with "general store", my email address preceded by the phrase: Do not forget that we are here if you need us My logo with the words "general store," my email address Preceded by the sentence: remember we're here if you need us (in french)
Nice to have
• i like this style: http://designpalettehub.com/inspiration/print-inspiration/25-beautiful-vintage-style-business-card-designs/ must feel the Vintage America it must feel the Vintage America lice can change a little logo or to color ... You can change the logo a little gold in color it could ... i like kraft paper with red ....
Should not have

```html
<!DOCTYPE html>
<html lang="fr">
<head>
<meta charset="utf-8">
<title>Le Comptoir du Bison Roux — cartes de visite</title>
<link rel="stylesheet" href="https://fonts.googleapis.com/css2?family=Marcellus&family=Courier+Prime&family=Rye&family=Old+Standard+TT&display=swap">
<style>
  :root {
    --backdrop: #e4e4e4;
    --kraft: #c8a676;
    --kraft-dark: #b8955f;
    --ink: #231b14;
    --rust: #9a3a1e;
    --art-tone: #8f7656;
    --stamp-tone: rgba(90, 70, 50, 0.35);
  }
  * { box-sizing: border-box; margin: 0; padding: 0; }
  html, body {
    width: 1200px; height: 900px; overflow: hidden;
    background: var(--backdrop);
  }
  .canvas { position: relative; width: 1200px; height: 900px; }
  .card {
    position: absolute; left: 361px; width: 482px; height: 289px;
    background: radial-gradient(circle at 40% 40%, var(--kraft) 0%, var(--kraft-dark) 100%);
    overflow: hidden;
  }
  .card--front { top: 149px; }
  .card--back { top: 482px; }
  .card__frame { position: absolute; inset: 0; width: 482px; height: 289px; }

  /* Front */
  .front__illustration {
    position: absolute; left: 119px; top: 55px; width: 224px; height: 112px;
    background: linear-gradient(180deg, rgba(143,118,86,0.55), rgba(90,70,50,0.7));
    border-radius: 4px;
  }
  .front__name {
    position: absolute; left: 0; width: 482px; top: 168px; text-align: center;
    font-family: "Marcellus", serif; font-size: 17px; letter-spacing: 0.5px;
    color: var(--rust);
  }
  .front__rule {
    position: absolute; left: 78px; top: 197px; width: 362px; height: 1px;
    background: var(--ink); opacity: 0.7;
  }
  .front__postmark {
    position: absolute; left: 341px; top: 165px; width: 100px; height: 100px;
    border-radius: 50%; border: 4px solid var(--stamp-tone);
  }

  /* Back */
  .back__badge {
    position: absolute; left: 87px; top: 64px; width: 120px; height: 120px;
    border-radius: 50%; border: 2px solid var(--ink);
    display: flex; align-items: center; justify-content: center; text-align: center;
    padding: 14px;
  }
  .back__badge-name {
    font-family: "Marcellus", serif; font-size: 15px; line-height: 1.25;
    color: var(--rust);
  }
  .back__message {
    position: absolute; left: 251px; top: 82px; width: 148px;
    font-family: "Courier Prime", monospace; font-size: 15.5px; line-height: 22px;
    color: var(--ink); text-align: justify; text-align-last: justify;
  }
  .back__initial { font-family: "Rye", serif; font-size: 19px; }
  .back__contact {
    position: absolute; left: 0; width: 482px; text-align: center;
    font-family: "Old Standard TT", serif; font-size: 15px; color: var(--rust);
  }
  .back__email { top: 200px; }
  .back__web { top: 227px; }
</style>
</head>
<body>
<main class="canvas">

  <section class="card card--front" aria-label="Recto de la carte">
    <svg class="card__frame" viewBox="0 0 482 289" aria-hidden="true">
      <g fill="none" stroke="var(--ink)" stroke-width="1.6">
        <line x1="40" y1="18" x2="180" y2="18"/><line x1="290" y1="18" x2="442" y2="18"/>
        <line x1="40" y1="271" x2="180" y2="271"/><line x1="290" y1="271" x2="442" y2="271"/>
        <line x1="18" y1="40" x2="18" y2="140"/><line x1="18" y1="152" x2="18" y2="250"/>
        <line x1="464" y1="40" x2="464" y2="140"/><line x1="464" y1="152" x2="464" y2="250"/>
        <circle cx="28" cy="30" r="9"/><circle cx="454" cy="30" r="9"/>
        <circle cx="28" cy="260" r="9"/><circle cx="454" cy="260" r="9"/>
      </g>
      <g fill="var(--ink)">
        <path d="M197 12l5 5-5 5-5-5z"/><path d="M234 12l5 5-5 5-5-5z"/><path d="M272 12l5 5-5 5-5-5z"/>
        <path d="M197 266l5 5-5 5-5-5z"/><path d="M234 266l5 5-5 5-5-5z"/><path d="M272 266l5 5-5 5-5-5z"/>
        <rect x="11" y="138" width="14" height="16" role="img" aria-label="Ornement latéral"/>
        <rect x="457" y="138" width="14" height="16" role="img" aria-label="Ornement latéral"/>
      </g>
    </svg>
    <div class="front__illustration" role="img" aria-label="Illustration d'une grange entourée de sapins"></div>
    <p class="front__name">LE COMPTOIR DU BISON ROUX</p>
    <div class="front__rule"></div>
    <div class="front__postmark" role="img" aria-label="Cachet postal décoratif"></div>
  </section>

  <section class="card card--back" aria-label="Verso de la carte">
    <svg class="card__frame" viewBox="0 0 482 289" aria-hidden="true">
      <g fill="none" stroke="var(--ink)" stroke-width="1.6">
        <line x1="40" y1="18" x2="180" y2="18"/><line x1="290" y1="18" x2="442" y2="18"/>
        <line x1="40" y1="271" x2="180" y2="271"/><line x1="290" y1="271" x2="442" y2="271"/>
        <line x1="18" y1="40" x2="18" y2="140"/><line x1="18" y1="152" x2="18" y2="250"/>
        <line x1="464" y1="40" x2="464" y2="140"/><line x1="464" y1="152" x2="464" y2="250"/>
        <circle cx="28" cy="30" r="9"/><circle cx="454" cy="30" r="9"/>
        <circle cx="28" cy="260" r="9"/><circle cx="454" cy="260" r="9"/>
      </g>
      <g fill="var(--ink)">
        <path d="M197 12l5 5-5 5-5-5z"/><path d="M234 12l5 5-5 5-5-5z"/><path d="M272 12l5 5-5 5-5-5z"/>
        <path d="M197 266l5 5-5 5-5-5z"/><path d="M234 266l5 5-5 5-5-5z"/><path d="M272 266l5 5-5 5-5-5z"/>
        <rect x="11" y="138" width="14" height="16" role="img" aria-label="Ornement latéral"/>
        <rect x="457" y="138" width="14" height="16" role="img" aria-label="Ornement latéral"/>
      </g>
    </svg>
    <div class="back__badge">
      <p class="back__badge-name">Le Comptoir du Bison Roux</p>
    </div>
    <p class="back__message"><span class="back__initial">N</span>'oubliez pas que nous sommes là, si vous avez besoin de nous</p>
    <p class="back__contact back__email">contact@lecomptoirdubisonroux.com</p>
    <p class="back__contact back__web">www.lecomptoirdubisonroux.com</p>
  </section>

</main>
</body>
</html>
```